Website Redesign Brief for Breezeline Cooling Services WA

Creating a clear and concise brief for designers to redesign your website, https://breezelinecowa.com.au/, is essential to ensure the project aligns with your vision for a more energetic, friendly, optimistic, and user-friendly website. Below is a sample brief tailored to your request, balancing specificity with flexibility to allow designers to bring their creativity to the table.

Website Redesign Brief for Breezeline Co WA
1. Project Overview

We are seeking a redesign of our website, https://breezelinecowa.com.au/, to create a vibrant, engaging, and user-friendly online presence that reflects our brand’s commitment to providing top-notch air conditioning services in Western Australia. The redesigned website should feel energetic, friendly, and optimistic while maintaining professionalism and improving user experience.
2. Goals and Objectives

Enhance Brand Perception: Convey a modern, approachable, and positive brand identity that resonates with both residential and commercial clients.
Improve User Experience: Simplify navigation, improve accessibility, and ensure a seamless experience across devices (desktop, tablet, mobile).
Increase Engagement: Encourage visitors to explore services, request quotes, and contact us through clear calls-to-action (CTAs).
Boost Conversion Rates: Make it easier for users to find information and take action (e.g., booking services or inquiries).
Showcase Expertise: Highlight our professional air conditioning services, experience, and customer satisfaction in an inviting way.

3. Target Audience

Primary Audience: Homeowners and small business owners in Western Australia seeking air conditioning installation, maintenance, or repair services.
Secondary Audience: Property managers, commercial clients, and real estate professionals looking for reliable HVAC solutions.
Demographics: Ages 25–65, mix of tech-savvy and non-tech-savvy users, located primarily in Perth and surrounding areas.
User Needs: Clear information about services, transparent pricing, easy contact options, and reassurance of quality and reliability.

4. Design Preferences

Tone and Style:

Energetic: Use bold, vibrant colors (e.g., blues, whites, and pops of warm tones like orange or yellow) to evoke energy and optimism.
Friendly: Incorporate approachable language, welcoming imagery, and a clean, uncluttered layout.
Optimistic: Highlight positive customer outcomes (e.g., comfort, energy savings) through visuals and messaging.
Professional yet approachable: Maintain credibility as a trusted service provider while avoiding a cold or overly corporate feel.

Visual Elements:

Use high-quality images of happy customers, comfortable homes/offices, and modern air conditioning units.
Incorporate subtle animations or micro-interactions to add energy (e.g., hover effects on buttons or smooth scrolling).
Avoid overly complex graphics that may slow down the site or distract from usability.

Typography: Clean, modern fonts that are easy to read. Use larger, bold headings for hierarchy and warmth.
Inspiration: Websites like https://www.frostvale.com.au/ (clean and professional) or https://www.quellarpowertech.com.au/ (user-friendly and modern) but with a more vibrant and welcoming vibe.

5. Functional Requirements

User-Friendly Navigation: Simplify the menu structure to make key pages (e.g., Services, About Us, Contact) easily accessible.
Mobile Responsiveness: Ensure the site is fully optimized for mobile devices, with fast load times and intuitive touch interactions.
Key Features:

Prominent CTAs for requesting quotes, booking services, or contacting the team.
A clear service overview with icons or visuals for each service (e.g., installation, repairs, maintenance).
A testimonials section to showcase customer satisfaction.
An easy-to-use contact form with minimal fields.
Integration with Google Maps for location-based services or office directions.

SEO and Performance: Optimize for search engines (e.g., keywords like “air conditioning Perth”) and ensure fast loading speeds.
Accessibility: Follow WCAG guidelines to ensure the site is usable for all visitors, including those with disabilities.

6. Content Guidance

Existing Content: Review and refine current content from https://breezelinecowa.com.au/ to make it concise, engaging, and aligned with the friendly tone.
New Content Ideas:

Add a “Why Choose Us” section highlighting expertise, customer service, and eco-friendly solutions.
Include a FAQ page to address common customer questions.
Create a blog section for tips on air conditioning maintenance or energy efficiency (optional).

Tone of Voice: Conversational, reassuring, and positive. Avoid technical jargon unless clearly explained.

7. Technical Considerations

Platform: Open to recommendations (e.g., WordPress, Wix, or custom-built) but prioritize ease of maintenance and scalability.
Integrations: Ensure compatibility with existing tools (e.g., Google Analytics, CRM for quote requests, or booking systems).
Domain and Hosting: Retain current domain (breezelinecowa.com.au); hosting recommendations welcome.
Timeline: Initial design concepts within [insert timeline, e.g., 2–3 weeks], with full redesign completed by [insert deadline, e.g., 6–8 weeks].
Budget: [Insert budget range or state “flexible, please provide a quote”].

8. Deliverables

Wireframes and mockups for homepage, service pages, and contact page.
Fully responsive website design with all necessary pages.
Style guide (colors, fonts, imagery guidelines).
CMS setup (if applicable) with basic training for content updates.
Testing and optimization for performance and SEO.

9. Success Metrics

Increased time on site and reduced bounce rate.
Higher conversion rates for quote requests and contact form submissions.
Positive user feedback on ease of navigation and overall experience.
Improved search engine rankings for key terms within [insert timeframe, e.g., 3 months].

10. Additional Notes

Please provide a portfolio of similar projects or examples of user-friendly, vibrant websites.
We are open to creative suggestions to make the website stand out in the HVAC industry.
Regular progress updates and collaboration during the design process are appreciated.
Updates

designers are asking for more time

few have requested an extension. I Have extended

Target Market(s)

Primary Audience: Homeowners and small business owners in Western Australia seeking air conditioning installation, maintenance, or repair services. Secondary Audience: Property managers, commercial clients, and real estate professionals looking for reliable HVAC solutions. Demographics: Ages 25–65, mix of tech-savvy and non-tech-savvy users, located primarily in Perth and surrounding areas. User Needs: Clear information about services, transparent pricing, easy contact options, and reassurance of quality and reliability.

Industry/Entity Type

Air Conditioning and Refrigeration (HVAC & R)

Coding

Coded - Design and coding required

Colors
0054AA
0677BA
7BADD7
CADEEF
E8F1F8
59FF00
82FF00
B8FF75
E3FFCB
F4FFEA
F0912C
F2A743
F7CA91
FBE8D2
FDF5EE
EE7325
F08F49
F5BC92
FAE3D3
FDF4ED

Requirements
Must have
• Must have all my current information I currently have on my web page.
Nice to have
• A sales page for people to buy products online

```html
<!DOCTYPE html>
<html lang="en">
<head>
<meta charset="utf-8">
<title>Coolwattle Cooling Services WA</title>
<link href="https://fonts.googleapis.com/css2?family=Montserrat:ital,wght@0,400;0,500;0,600;0,700;1,400;1,600&display=swap" rel="stylesheet">
<style>
:root{
  --navy:#223b62;
  --navy-deep:#1b3155;
  --orange:#EE7325;
  --orange-soft:#F08F49;
  --ink:#1f3a60;
  --text:#555b66;
  --line:#dfe3ea;
  --grey-bg:#f5f6f8;
  --white:#ffffff;
}
*{margin:0;padding:0;box-sizing:border-box}
html,body{width:1200px;height:5396px;overflow:hidden}
body{font-family:"Montserrat",sans-serif;color:var(--text);background:var(--white);position:relative}
section,header,footer{position:absolute;left:0;width:1200px}
.abs{position:absolute}
.eyebrow{font-size:13px;color:var(--orange);font-weight:500}
.eyebrow.center,.title.center{text-align:center;width:100%;left:0}
.title{font-size:34px;font-weight:700;color:var(--ink);text-transform:uppercase;letter-spacing:.3px}
.light .title{color:var(--white)}
.light .eyebrow{color:#dfe6f1}
.btn{background:var(--orange);color:var(--white);font-weight:600;font-size:13px;text-transform:uppercase;border-radius:22px;display:flex;align-items:center;justify-content:center}
.read-more{font-size:11.5px;font-weight:700;font-style:italic;text-decoration:underline;text-transform:uppercase;color:var(--orange)}
.photo{position:absolute}

/* header */
.site-header{top:0;height:84px;background:var(--white);box-shadow:0 1px 0 #eceef2}
.logo{left:61px;top:27px;display:flex;align-items:center;gap:8px}
.logo .mark{width:30px;height:30px;border-radius:50%;background:var(--orange)}
.logo span{font-size:19px;font-weight:700;color:var(--navy)}
.nav a{position:absolute;top:36px;font-size:13px;color:var(--ink);text-decoration:none}
.nav a.active{color:var(--orange)}
.header-btn{left:970px;top:23px;width:170px;height:42px;font-size:13px}

/* hero */
.hero{top:84px;height:591px}
.hero-photo{inset:0;background:linear-gradient(100deg,#f4f2ef 0%,#ece6df 45%,#c9b8a4 75%,#8e7560 100%)}
.hero h1{left:61px;top:166px;font-size:43px;line-height:53px;font-weight:700;color:var(--ink);text-transform:uppercase}
.hero p{left:61px;top:287px;width:480px;font-size:15px;line-height:22px;color:#2c3a52}
.hero .btn{left:61px;top:381px;width:172px;height:40px;font-size:13px}
.contact-bar{left:197px;top:548px;width:814px;height:84px;border-radius:42px;overflow:hidden;background:var(--navy)}
.contact-bar .call,.contact-bar .mail{position:absolute;top:0;height:84px;display:flex;align-items:center;gap:18px;color:var(--white);font-size:17px}
.contact-bar .call{left:42px}
.contact-bar .mail{left:382px;right:0;background:var(--orange);border-radius:42px 0 0 42px;padding-left:32px}

/* about */
.about{top:675px;height:571px}
.about-main{left:124px;top:108px;width:341px;height:342px;border-radius:8px;background:linear-gradient(135deg,#e9ecef,#b9c2cc 55%,#5d6d80)}
.about-second{left:278px;top:271px;width:283px;height:222px;border-radius:8px;border:6px solid var(--white);background:linear-gradient(135deg,#f3e6da,#d7b79a 60%,#a9836a)}
.about .eyebrow{left:639px;top:123px}
.about .title{left:639px;top:152px;font-size:34px}
.about p{left:639px;top:198px;width:424px;font-size:12.5px;line-height:22px}
.about-video{left:637px;top:328px;width:134px;height:82px;border-radius:8px;background:linear-gradient(135deg,#c9d2dc,#6e7e90)}
.about-video .play{position:absolute;left:52px;top:26px;width:30px;height:30px;border-radius:50%;background:var(--white);display:flex;align-items:center;justify-content:center}
.about-call{left:793px;top:350px;display:flex;align-items:center;gap:14px}
.about-call .ic{width:36px;height:36px;border-radius:50%;background:var(--orange);display:flex;align-items:center;justify-content:center}
.about-call small{display:block;font-size:11.5px;color:var(--ink)}
.about-call b{font-size:16px;color:var(--ink)}
.about .btn{left:637px;top:437px;width:136px;height:40px}

/* services */
.services{top:1246px;height:812px;background:linear-gradient(180deg,#2a4570,#223b62 40%,#1e3559)}
.services .eyebrow{top:84px}
.services .title{top:112px}
.service-card{position:absolute;width:257px;height:272px;border-radius:10px;background:var(--navy-deep);border:1px solid rgba(255,255,255,.08);padding:0 22px}
.service-card.featured{background:var(--orange)}
.service-card svg{position:absolute;left:22px;top:35px}
.service-card h3{position:absolute;left:22px;top:109px;font-size:16px;font-weight:600;color:var(--white)}
.service-card p{position:absolute;left:22px;top:141px;width:215px;font-size:12.5px;line-height:22px;color:#e3e8f0}
.service-card .read-more{position:absolute;left:22px;top:221px;color:var(--orange)}
.service-card.featured .read-more{color:var(--white)}
.services-photo{left:607px;top:465px;width:532px;height:272px;border-radius:10px;background:linear-gradient(120deg,#efe9e3,#d9c6b3 55%,#9f8a77)}

/* why */
.why{top:2058px;height:469px}
.why .eyebrow{top:80px}
.why .title{top:112px}
.why-item{position:absolute;top:174px;width:250px;text-align:center}
.why-item .badge{width:94px;height:94px;border-radius:50%;margin:0 auto;background:var(--orange);border:5px solid #fbe3d3;display:flex;align-items:center;justify-content:center}
.why-item h3{margin-top:28px;font-size:16px;font-weight:600;color:var(--ink)}
.why-item p{margin-top:10px;font-size:12.5px;line-height:22px}
.why-item .read-more{display:block;margin-top:8px}

/* faq */
.faq{top:2527px;height:535px;background:var(--navy)}
.faq-photo{left:0;top:0;width:599px;height:535px;background:linear-gradient(135deg,#eef0f2,#c5ccd4 50%,#8f9aa7)}
.faq .eyebrow{left:647px;top:82px}
.faq .title{left:647px;top:110px}
.faq-item{position:absolute;left:647px;width:493px;border-bottom:1px solid rgba(255,255,255,.2);font-size:13px;color:var(--white)}
.faq-item .q{display:flex;justify-content:space-between;align-items:center;height:22px}
.faq-item.open .q{color:var(--orange);font-weight:600;font-size:14px}
.faq-item .a{font-size:12.5px;line-height:22px;color:#dde4ee;margin-top:6px;width:470px}

/* testimonials */
.testimonials{top:3062px;height:491px}
.testimonials .eyebrow{top:77px}
.testimonials .title{top:111px}
.review{position:absolute;top:173px;width:448px;height:243px;background:var(--grey-bg);border-radius:10px}
.review p{position:absolute;left:42px;top:42px;width:380px;font-size:13px;line-height:22px;font-style:italic;color:#5e6470}
.review .avatar{position:absolute;left:42px;top:146px;width:62px;height:62px;border-radius:50%;background:linear-gradient(135deg,#e5d8cc,#a88d78)}
.review .who{position:absolute;left:140px;top:160px;font-size:14px;font-weight:600;color:var(--ink)}
.review .stars{position:absolute;left:140px;top:184px;display:flex;gap:3px}
.arrow-btn{position:absolute;width:38px;height:38px;border-radius:50%;display:flex;align-items:center;justify-content:center}
.arrow-btn.prev{left:58px;top:273px;background:var(--orange)}
.arrow-btn.next{left:1101px;top:273px;border:1.5px solid var(--ink);background:var(--white)}

/* brands */
.brands{top:3553px;height:369px;background:linear-gradient(180deg,#2c4772,#223b62)}
.brands .eyebrow{top:84px}
.brands .title{top:116px}
.brand-tile{position:absolute;top:174px;width:206px;height:120px;background:var(--white);border-radius:4px;display:flex;align-items:center;justify-content:center;gap:8px;font-size:16px;font-weight:700;color:var(--navy)}
.brand-tile i{width:14px;height:14px;border-radius:50%;background:var(--orange);display:block;flex:none}
.brands .chev{position:absolute;top:222px}

/* blog */
.blog{top:3922px;height:622px}
.blog .eyebrow{top:83px}
.blog .title{top:115px}
.post{position:absolute;top:176px;width:350px;height:369px;background:var(--white);border-radius:8px;box-shadow:0 4px 18px rgba(30,50,90,.09);overflow:hidden}
.post .img{position:absolute;left:0;top:0;width:350px;height:174px}
.post .meta{position:absolute;left:0;top:174px;width:350px;height:29px;background:var(--navy);color:var(--white);font-size:11.5px;display:flex;align-items:center;gap:22px;padding-left:26px}
.post .meta span{display:flex;align-items:center;gap:7px}
.post.first .meta{background:var(--orange)}
.post h3{position:absolute;left:26px;top:236px;font-size:16px;font-weight:600;color:var(--ink)}
.post p{position:absolute;left:26px;top:266px;width:300px;font-size:12.5px;line-height:22px}
.post .read-more{position:absolute;left:26px;top:322px}

/* contact */
.contact{top:4544px;height:534px}
.contact-photo{inset:0;background:linear-gradient(100deg,#9d8570 0%,#cdb9a6 35%,#ece6e0 55%,#f4f2f0 100%)}
.contact .eyebrow{left:660px;top:84px}
.contact .title{left:660px;top:112px}
.field{position:absolute;left:660px;width:390px;height:38px;border:1px solid #c9ccd2;border-radius:6px;background:var(--white);font-size:11.5px;color:#666;padding:11px 12px}
.field.first{border-color:#777}
.field.msg{height:90px}
.contact .btn{left:660px;top:419px;width:126px;height:40px}

/* footer */
.site-footer{top:5078px;height:318px;background:var(--navy);color:var(--white)}
.site-footer h4{position:absolute;font-size:17px;font-weight:600;color:var(--orange)}
.foot-links{position:absolute;left:61px;top:100px;list-style:none;font-size:12.5px;line-height:22.6px}
.foot-logo{left:0;width:1200px;top:72px;display:flex;justify-content:center;align-items:center;gap:8px}
.foot-logo .mark{width:26px;height:26px;border-radius:50%;background:var(--orange)}
.foot-logo span{font-size:19px;font-weight:700;color:var(--white)}
.foot-about{left:0;width:1200px;top:148px;text-align:center;font-size:12.5px;line-height:22px}
.socials{left:0;width:1200px;top:212px;display:flex;justify-content:center;gap:14px}
.socials i{width:32px;height:32px;border-radius:50%;background:var(--orange);display:block}
.foot-contact{position:absolute;left:882px;display:flex;align-items:center;gap:18px;font-size:12.5px;line-height:20px}
.foot-contact .ic{width:32px;height:32px;border-radius:50%;background:var(--orange);display:flex;align-items:center;justify-content:center;flex:none}
.copyright{left:0;width:1200px;top:288px;text-align:center;font-size:12px;color:#e2e7ef}
</style>
</head>
<body>

<header class="site-header">
  <div class="abs logo"><i class="mark"></i><span>Coolwattle</span></div>
  <nav class="nav">
    <a class="active" style="left:298px">Home</a>
    <a style="left:384px">About Us</a>
    <a style="left:488px">Services</a>
    <a style="left:588px">Why Choose Us</a>
    <a style="left:736px">FAQ</a>
    <a style="left:805px">Blog</a>
    <a style="left:880px">Contact</a>
  </nav>
  <div class="abs btn header-btn">Book a Services</div>
</header>

<section class="hero">
  <div class="photo hero-photo" role="img" aria-label="Smiling family relaxing at home beneath a wall-mounted air conditioner"></div>
  <h1 class="abs">Quality Air<br>Conditioning Services</h1>
  <p class="abs">Our service is second to none; we have a team of experienced technicians that consistently deliver the best quality air conditioner repairs Perth has to offer.</p>
  <div class="abs btn">Book a Services</div>
  <div class="abs contact-bar">
    <div class="call">
      <svg width="44" height="44" viewBox="0 0 44 44" fill="none" stroke="#fff" stroke-width="2"><circle cx="22" cy="22" r="19"/><path d="M16 14c-2 1-3 3-2 6 2 5 6 9 10 10 3 1 5 0 6-2l-3-3-3 1c-2-1-4-3-5-5l1-3z"/></svg>
      <span>Call Now : + 0400 555 019</span>
    </div>
    <div class="mail">
      <svg width="44" height="44" viewBox="0 0 44 44" fill="none" stroke="#fff" stroke-width="2"><rect x="8" y="12" width="28" height="20" rx="2"/><path d="M8 14l14 10 14-10"/></svg>
      <span>info@coolwattleair.com</span>
    </div>
  </div>
</section>

<section class="about">
  <div class="photo about-main" role="img" aria-label="Air conditioning technician in overalls giving a thumbs up"></div>
  <div class="photo about-second" role="img" aria-label="Father lifting his daughter in a cool living room"></div>
  <div class="abs eyebrow">About Us</div>
  <h2 class="abs title">Air Conditioning</h2>
  <p class="abs">Our service is second to none; our team of experienced technicians that consistently deliver the best quality air conditioner repairs Perth has to offer. There are many different brands of air conditioning on the market, each with their own way of controlling the temperature of your home.</p>
  <div class="abs about-video" role="img" aria-label="Video preview of a technician servicing an air conditioner">
    <div class="play"><svg width="12" height="12" viewBox="0 0 12 12"><path d="M3 1l8 5-8 5z" fill="#EE7325"/></svg></div>
  </div>
  <div class="abs about-call">
    <div class="ic"><svg width="18" height="18" viewBox="0 0 24 24" fill="#fff"><path d="M6 3c-2 1-3 3-2 7 2 5 6 9 11 11 4 1 6 0 7-2l-4-4-3 1c-2-1-5-4-6-6l1-3z"/></svg></div>
    <div><small>Call to Action</small><b>+ 0400 555 019</b></div>
  </div>
  <div class="abs btn">View More</div>
</section>

<section class="services light">
  <div class="abs eyebrow center">Some Of Speciality</div>
  <h2 class="abs title center">Our Services</h2>

  <article class="service-card" style="left:61px;top:176px">
    <svg width="46" height="46" viewBox="0 0 46 46" fill="none" stroke="#fff" stroke-width="2"><rect x="6" y="14" width="14" height="28"/><rect x="20" y="6" width="18" height="36"/><path d="M24 12h10M24 18h10M24 24h10M24 30h10M10 20h6M10 26h6M10 32h6M2 42h42"/></svg>
    <h3>Commercial Installation</h3>
    <p>Lorem Ipsum has been the industry's standard dummy text ever since the 1500s.</p>
    <span class="read-more">Read More</span>
  </article>
  <article class="service-card featured" style="left:335px;top:176px">
    <svg width="58" height="46" viewBox="0 0 58 46" fill="none" stroke="#fff" stroke-width="2"><rect x="3" y="8" width="52" height="18" rx="3"/><path d="M9 20h40M16 32l-2 8M24 32l-1 8M34 32l1 8M42 32l2 8"/></svg>
    <h3>Domestic Installation</h3>
    <p>Lorem Ipsum has been the industry's standard dummy text ever since the 1500s.</p>
    <span class="read-more">Read More</span>
  </article>
  <article class="service-card" style="left:607px;top:176px">
    <svg width="58" height="46" viewBox="0 0 58 46" fill="none" stroke="#fff" stroke-width="2"><rect x="3" y="6" width="52" height="20" rx="3"/><path d="M9 20h40M29 28v16M22 32l14 8M36 32l-14 8"/></svg>
    <h3>Coolroom Installation</h3>
    <p>Lorem Ipsum has been the industry's standard dummy text ever since the 1500s.</p>
    <span class="read-more">Read More</span>
  </article>
  <article class="service-card" style="left:882px;top:176px">
    <svg width="58" height="46" viewBox="0 0 58 46" fill="none" stroke="#fff" stroke-width="2"><rect x="8" y="12" width="42" height="26" rx="3"/><circle cx="29" cy="25" r="8"/><path d="M29 17v16M21 25h16M14 6h30M8 42h42"/></svg>
    <h3>Chiller Service &amp; Repairs</h3>
    <p>Lorem Ipsum has been the industry's standard dummy text ever since the 1500s.</p>
    <span class="read-more">Read More</span>
  </article>
  <article class="service-card" style="left:61px;top:465px">
    <svg width="58" height="46" viewBox="0 0 58 46" fill="none" stroke="#fff" stroke-width="2"><rect x="3" y="6" width="52" height="18" rx="3"/><path d="M9 18h40M14 30v12M22 30v8M30 30v12M38 30v8"/></svg>
    <h3>Air Quality Control</h3>
    <p>Lorem Ipsum has been the industry's standard dummy text ever since the 1500s.</p>
    <span class="read-more">Read More</span>
  </article>
  <article class="service-card" style="left:335px;top:465px">
    <svg width="58" height="46" viewBox="0 0 58 46" fill="none" stroke="#fff" stroke-width="2"><circle cx="29" cy="24" r="9"/><path d="M29 4v8M29 36v8M9 24h8M41 24h8M15 10l6 6M37 32l6 6M43 10l-6 6M21 32l-6 6"/></svg>
    <h3>BMS Upgrades</h3>
    <p>Lorem Ipsum has been the industry's standard dummy text ever since the 1500s.</p>
    <span class="read-more">Read More</span>
  </article>
  <div class="photo services-photo" role="img" aria-label="Family sitting together on a sofa below a split system air conditioner"></div>
</section>

<section class="why">
  <div class="abs eyebrow center">Our Process</div>
  <h2 class="abs title center">Why Chooes Us</h2>
  <div class="why-item" style="left:200px">
    <div class="badge"><svg width="40" height="40" viewBox="0 0 40 40" fill="none" stroke="#fff" stroke-width="2"><circle cx="20" cy="16" r="10"/><path d="M14 25l-4 12 6-3 4 5 2-13M26 25l4 12-6-3"/><path d="M20 11l1.5 3 3.5.5-2.5 2.5.5 3.5-3-1.5-3 1.5.5-3.5-2.5-2.5 3.5-.5z"/></svg></div>
    <h3>Expertise</h3>
    <p>Lorem Ipsum has been the industry's standard dummy.</p>
    <span class="read-more">Read More</span>
  </div>
  <div class="why-item" style="left:474px">
    <div class="badge"><svg width="40" height="40" viewBox="0 0 40 40" fill="none" stroke="#fff" stroke-width="2"><circle cx="20" cy="20" r="15"/><circle cx="20" cy="16" r="5"/><path d="M11 30c2-5 5-7 9-7s7 2 9 7"/></svg></div>
    <h3>Customer Service</h3>
    <p>Lorem Ipsum has been the industry's standard dummy.</p>
    <span class="read-more">Read More</span>
  </div>
  <div class="why-item" style="left:748px">
    <div class="badge"><svg width="40" height="40" viewBox="0 0 40 40" fill="none" stroke="#fff" stroke-width="2"><path d="M20 36V18M20 24c-6 0-10-4-10-10 6 0 10 4 10 10zM20 20c0-6 4-10 10-10 0 6-4 10-10 10zM8 36h24"/></svg></div>
    <h3>Eco-friendly Solutions</h3>
    <p>Lorem Ipsum has been the industry's standard dummy.</p>
    <span class="read-more">Read More</span>
  </div>
</section>

<section class="faq light">
  <div class="photo faq-photo" role="img" aria-label="Happy family playing together in a bright air-conditioned room"></div>
  <div class="abs eyebrow">FAQs</div>
  <h2 class="abs title">Have Any Questions?</h2>
  <div class="faq-item open" style="top:168px;height:94px">
    <div class="q">How often should I service my air conditioner?<svg width="14" height="14" viewBox="0 0 14 14" fill="none" stroke="#fff" stroke-width="1.6"><path d="M3 9l4-4 4 4"/></svg></div>
    <div class="a">It's recommended to service your AC at least once a year to ensure efficiency, prevent breakdowns, and extend its lifespan.</div>
  </div>
  <div class="faq-item" style="top:272px;height:42px"><div class="q">How long does an air conditioner typically last?<svg width="14" height="14" viewBox="0 0 14 14" fill="none" stroke="#fff" stroke-width="1.6"><path d="M3 5l4 4 4-4"/></svg></div></div>
  <div class="faq-item" style="top:326px;height:42px"><div class="q">What size AC unit do I need for my home?<svg width="14" height="14" viewBox="0 0 14 14" fill="none" stroke="#fff" stroke-width="1.6"><path d="M3 5l4 4 4-4"/></svg></div></div>
  <div class="faq-item" style="top:380px;height:42px"><div class="q">Why is my air conditioner not cooling properly?<svg width="14" height="14" viewBox="0 0 14 14" fill="none" stroke="#fff" stroke-width="1.6"><path d="M3 5l4 4 4-4"/></svg></div></div>
  <div class="faq-item" style="top:434px;height:42px;border-bottom:none"><div class="q">How often should I change my AC filter?<svg width="14" height="14" viewBox="0 0 14 14" fill="none" stroke="#fff" stroke-width="1.6"><path d="M3 5l4 4 4-4"/></svg></div></div>
</section>

<section class="testimonials">
  <div class="abs eyebrow center">Testimonial</div>
  <h2 class="abs title center">Customer Feedback</h2>
  <div class="arrow-btn prev"><svg width="14" height="14" viewBox="0 0 14 14"><path d="M9 2L4 7l5 5z" fill="#fff"/></svg></div>
  <article class="review" style="left:142px">
    <p>Lorem Ipsum has been the industry's standard dummy text ever since the 1500s, when an unknown printer took a galley of type and scrambled it to make a type specimen book.</p>
    <div class="avatar" role="img" aria-label="Client portrait"></div>
    <div class="who">- Client Name</div>
    <div class="stars"><svg width="80" height="13" viewBox="0 0 80 13" fill="#EE7325"><path id="st" d="M6.5 0l2 4.2 4.5.6-3.3 3.1.8 4.6-4-2.2-4 2.2.8-4.6L0 4.8l4.5-.6z"/><use href="#st" x="16.5"/><use href="#st" x="33"/><use href="#st" x="49.5"/><use href="#st" x="66"/></svg></div>
  </article>
  <article class="review" style="left:607px">
    <p>Lorem Ipsum has been the industry's standard dummy text ever since the 1500s, when an unknown printer took a galley of type and scrambled it to make a type specimen book.</p>
    <div class="avatar" role="img" aria-label="Client portrait"></div>
    <div class="who">- Client Name</div>
    <div class="stars"><svg width="80" height="13" viewBox="0 0 80 13" fill="#EE7325"><path id="st2" d="M6.5 0l2 4.2 4.5.6-3.3 3.1.8 4.6-4-2.2-4 2.2.8-4.6L0 4.8l4.5-.6z"/><use href="#st2" x="16.5"/><use href="#st2" x="33"/><use href="#st2" x="49.5"/><use href="#st2" x="66"/></svg></div>
  </article>
  <div class="arrow-btn next"><svg width="14" height="14" viewBox="0 0 14 14"><path d="M5 2l5 5-5 5z" fill="#1f3a60"/></svg></div>
</section>

<section class="brands light">
  <div class="abs eyebrow center">Brands</div>
  <h2 class="abs title center">Our Recommended Brands</h2>
  <svg class="chev" style="left:109px" width="14" height="24" viewBox="0 0 14 24" fill="none" stroke="#fff" stroke-width="2"><path d="M11 3L3 12l8 9"/></svg>
  <div class="brand-tile" style="left:165px"><i></i>Norvane Climate</div>
  <div class="brand-tile" style="left:385px"><i></i>Frostvale</div>
  <div class="brand-tile" style="left:607px"><i></i>Aerolith</div>
  <div class="brand-tile" style="left:829px"><i></i>Quellar Powertech</div>
  <svg class="chev" style="left:1083px" width="14" height="24" viewBox="0 0 14 24" fill="none" stroke="#fff" stroke-width="2"><path d="M3 3l8 9-8 9"/></svg>
</section>

<section class="blog">
  <div class="abs eyebrow center">New Post</div>
  <h2 class="abs title center">Latest Blogs</h2>
  <article class="post first" style="left:59px">
    <div class="img" role="img" aria-label="Technician repairing an outdoor condenser unit" style="background:linear-gradient(135deg,#eef0f2,#c3c9cf 50%,#c7463a)"></div>
    <div class="meta"><span><svg width="12" height="12" viewBox="0 0 12 12" fill="none" stroke="#fff"><rect x="1" y="2" width="10" height="9"/><path d="M1 5h10"/></svg>07-jun-2025</span><span><svg width="12" height="12" viewBox="0 0 12 12" fill="none" stroke="#fff"><circle cx="6" cy="4" r="2.5"/><path d="M1.5 11c1-3 8-3 9 0"/></svg>Specia</span></div>
    <h3>Lorem Ipsum</h3>
    <p>Lorem Ipsum has been the industry's standard dummy text ever since the 1500s.</p>
    <span class="read-more">Read More</span>
  </article>
  <article class="post" style="left:423px">
    <div class="img" role="img" aria-label="Technician servicing an indoor split system" style="background:linear-gradient(135deg,#f2f3f5,#cfd6de 55%,#3f63a8)"></div>
    <div class="meta"><span><svg width="12" height="12" viewBox="0 0 12 12" fill="none" stroke="#fff"><rect x="1" y="2" width="10" height="9"/><path d="M1 5h10"/></svg>07-jun-2025</span><span><svg width="12" height="12" viewBox="0 0 12 12" fill="none" stroke="#fff"><circle cx="6" cy="4" r="2.5"/><path d="M1.5 11c1-3 8-3 9 0"/></svg>Specia</span></div>
    <h3>Lorem Ipsum</h3>
    <p>Lorem Ipsum has been the industry's standard dummy text ever since the 1500s.</p>
    <span class="read-more">Read More</span>
  </article>
  <article class="post" style="left:789px">
    <div class="img" role="img" aria-label="Technician in high-visibility gear checking rooftop units" style="background:linear-gradient(135deg,#e8e4dc,#b3a793 50%,#e07b35)"></div>
    <div class="meta"><span><svg width="12" height="12" viewBox="0 0 12 12" fill="none" stroke="#fff"><rect x="1" y="2" width="10" height="9"/><path d="M1 5h10"/></svg>07-jun-2025</span><span><svg width="12" height="12" viewBox="0 0 12 12" fill="none" stroke="#fff"><circle cx="6" cy="4" r="2.5"/><path d="M1.5 11c1-3 8-3 9 0"/></svg>Specia</span></div>
    <h3>Lorem Ipsum</h3>
    <p>Lorem Ipsum has been the industry's standard dummy text ever since the 1500s.</p>
    <span class="read-more">Read More</span>
  </article>
</section>

<section class="contact">
  <div class="photo contact-photo" role="img" aria-label="Laughing father carrying his child on his back"></div>
  <div class="abs eyebrow">Contact Us</div>
  <h2 class="abs title">Get In Touch</h2>
  <div class="field first" style="top:163px">Name *</div>
  <div class="field" style="top:211px">Email *</div>
  <div class="field" style="top:259px">Phone *</div>
  <div class="field msg" style="top:308px">Message *</div>
  <div class="abs btn">Submit</div>
</section>

<footer class="site-footer">
  <h4 style="left:61px;top:62px">Navigation</h4>
  <ul class="foot-links">
    <li>Home</li><li>About</li><li>Service</li><li>Why chooes us</li><li>Faqs</li><li>Blogs</li><li>Contact</li>
  </ul>
  <div class="abs foot-logo"><i class="mark"></i><span>Coolwattle</span></div>
  <p class="abs foot-about">Lorem Ipsum has been the industry's<br>standard dummy text eve</p>
  <div class="abs socials"><i></i><i></i><i></i></div>
  <h4 style="left:882px;top:46px">Contact</h4>
  <div class="foot-contact" style="top:89px"><span class="ic"><svg width="14" height="14" viewBox="0 0 24 24" fill="#fff"><path d="M6 3c-2 1-3 3-2 7 2 5 6 9 11 11 4 1 6 0 7-2l-4-4-3 1c-2-1-5-4-6-6l1-3z"/></svg></span>+ 0400 555 019</div>
  <div class="foot-contact" style="top:141px"><span class="ic"><svg width="14" height="14" viewBox="0 0 24 24" fill="none" stroke="#fff" stroke-width="2"><rect x="3" y="5" width="18" height="14"/><path d="M3 6l9 7 9-7"/></svg></span>info@coolwattleair.com</div>
  <div class="foot-contact" style="top:192px"><span class="ic"><svg width="14" height="14" viewBox="0 0 24 24" fill="#fff"><path d="M12 2a7 7 0 0 0-7 7c0 5 7 13 7 13s7-8 7-13a7 7 0 0 0-7-7zm0 10a3 3 0 1 1 0-6 3 3 0 0 1 0 6z"/></svg></span>27 Larkspur Road, Coolgrove WA<br>6170</div>
  <p class="abs copyright">Copyright © 2025 Air Conditioning. All Rights Reserved.</p>
</footer>

</body>
</html>
```